UPDATED BRIEF: Hypermobile EDS Book Cover Contest

I am writing a print book. I need cover designs to evaluate with your creativity. It is a nonfiction memoir meets self-help guide to living with a rare, incurable chronic illness called EDS. See attached Word doc for book details and copy. It is designed to be an inspiration story of living well with this disease so mindset is a key theme. I'm looking for all types of ideas including photography (sailboat, mountain, journey concepts), type flat designs highlighting hypermobility (a key part of the disease), including good use of color and white space. I want it to be legible, intriguing, and emotive if possible. I need someone to be able to produce and provide the production files and/or edit the final text back copy as it is not yet final. I will be sharing the contest with my fan base. I will ultimately need the cover, back cover, spine, and audio and ebook covers done all the same just reformatted to size. Print book 6x9 to be done first. I dont want to provide too much direction so you can be creative.
Updates

I uploaded a new brief for updated author name and back cover. Please update and I will start the poll. I will also extend the project timeline.

Can anyone create a design with the typeset words of hypermobile on the title being "pinched" by a string? Like holding it all together by a string?

Went on vacation/holiday

Target Market(s)

chronic illness disease victims, specifically those with Hypermobile Ehlers Danlos Syndrome (EDS), dysautonomia (POTS) or craniocervical instability in the neck

Industry/Entity Type

Self help, personal development, memoir

Font styles to use
Sans Serif

Colors
FFC000
F8CF3A
FAE287
FDF2CF
FEFAEE

Requirements
Must have
• legible, intriguing even emotive design with text or photos
Nice to have
• Potentially visually showing a journey, hypermobility, or overcoming obstacles
Should not have
• black dark backgrounds

```html
<!DOCTYPE html>
<html lang="en">
<head>
<meta charset="UTF-8">
<title>Keeping It All in Place When You're Extra Bendy – Book Cover</title>
<link href="https://fonts.googleapis.com/css2?family=Montserrat:wght@500;600;700;800&display=swap" rel="stylesheet">
<style>
  :root {
    --page-bg: #eeede8;
    --sky-top: #6c7ea6;
    --sky-mid: #a79aa8;
    --glow: #f3b46b;
    --glow-light: #fbe2b4;
    --haze: #c9c7c2;
    --mountain: #6f8193;
    --hill: #7d8c4e;
    --hill-deep: #56663a;
    --path: #b59c7c;
    --title-dark: #1f2436;
    --title-gold: #f0c419;
    --text-light: #ffffff;
  }
  * { margin: 0; padding: 0; box-sizing: border-box; }
  html, body {
    width: 1200px;
    height: 1200px;
    overflow: hidden;
    background: var(--page-bg);
  }
  .canvas {
    position: relative;
    width: 1200px;
    height: 1200px;
    display: flex;
    align-items: center;
    justify-content: center;
  }
  .book-cover {
    position: relative;
    width: 680px;
    height: 960px;
    overflow: hidden;
    font-family: 'Montserrat', Arial, sans-serif;
    text-align: center;
  }
  .cover-photo {
    position: absolute;
    inset: 0;
    background:
      radial-gradient(ellipse 70% 28% at 50% 46%, var(--glow-light) 0%, rgba(251,226,180,0) 70%),
      linear-gradient(180deg,
        var(--sky-top) 0%,
        var(--sky-mid) 18%,
        var(--glow) 34%,
        var(--glow-light) 46%,
        var(--haze) 54%,
        var(--mountain) 60%,
        var(--hill) 70%,
        var(--path) 82%,
        var(--hill-deep) 100%);
  }
  .subtitle {
    position: absolute;
    top: 28px;
    left: 0;
    right: 0;
    color: var(--text-light);
    font-weight: 500;
    font-size: 22px;
    line-height: 1.4;
    letter-spacing: 0.2px;
  }
  .title-lead {
    position: absolute;
    top: 200px;
    left: 0;
    right: 0;
    color: var(--title-dark);
    font-weight: 700;
    font-size: 29px;
    line-height: 1.45;
    letter-spacing: 0.5px;
  }
  .title-main {
    position: absolute;
    top: 283px;
    left: 0;
    right: 0;
    color: var(--title-gold);
    font-weight: 700;
    font-size: 112px;
    line-height: 0.92;
    letter-spacing: 1px;
    text-shadow: 3px 4px 6px rgba(40, 30, 10, 0.45);
  }
  .author {
    position: absolute;
    top: 868px;
    left: 0;
    right: 0;
    color: var(--text-light);
    font-weight: 600;
    font-size: 26px;
    letter-spacing: 2px;
  }
</style>
</head>
<body>
  <div class="canvas">
    <section class="book-cover">
      <div class="cover-photo" role="img" aria-label="Photograph of a dirt path lined with rustic wooden rails leading over green hills toward mountains and a lake under a glowing sunset sky"></div>
      <p class="subtitle">Find a Steadier, Brighter Everyday<br>with EDS, POTS, and Instability</p>
      <h1>
        <span class="title-lead">KEEPING IT ALL<br>IN PLACE WHEN YOU’RE</span>
        <span class="title-main">EXTRA<br>BENDY</span>
      </h1>
      <p class="author">MARLA J. HENSLEY</p>
    </section>
  </div>
</body>
</html>
```